Trucking company specializing in intermodal containers

We need a logo design for our trucking company based in Kent, Washington. Our companies name is Dorvale Haulworks LLC, we specialize in intermodal containers, and work off of the Crestmark rail lines and the ports. We provide service by transporting freight with our fleet of trucks. We operate within Washington, Oregon, and Idaho. Our fleet consists of an east division and a local division. Our team motto currently is globally connected, locally invested.

Target Market(s)

brokers, intermodal management companies, customers

Industry/Entity Type

Trucking Company

Contact Information for Business Card

physical address 4519 N. 163rd Pl Kent, WA 98517
office number is 253-614-9026

Font styles to use
Sans Serif

Colors

Designer to choose colors to be used in the design.

Requirements
Must have
• We need to update our current logo. Something like an emblem; that makes a statement that this logo/ sign represents Dorvale Haulworks. Something like a royal stamp but in this case a royal shield.
Nice to have
• simple, yet bold. something someone does not currently have. We need something fresh and exciting. Something that will also make a statement because currently our reputation is great within the industry and our community. But we need to reflect that we are professional and willing to provide the best service. We are open to new statement lines.
Should not have
• Should not have something thats been used before. We are open to suggestions that you have and a design that is completely unique and you make originally without what we want but what you like as well. Ofcourse it should still represent the industry we are in.

```html
<!DOCTYPE html>
<html lang="en">
<head>
<meta charset="utf-8">
<title>Dorvale Haulworks LLC – Business Cards and Emblem</title>
<link rel="stylesheet" href="https://fonts.googleapis.com/css2?family=Open+Sans:wght@300;400;700&display=swap">
<style>
  :root {
    --stage-top: #4a403b;
    --stage-bottom: #2c2623;
    --card: #2a2a2a;
    --card-edge: #1e1e1e;
    --ink-light: #f2f2f2;
    --ink-soft: #d6d6d6;
    --icon: #8d8d8d;
    --band-light: #f4f4f4;
    --band-dark: #d2d2d2;
    --emblem-red: #b8202d;
    --emblem-orange: #f07a1a;
  }
  * { box-sizing: border-box; margin: 0; padding: 0; }
  html, body { width: 1200px; height: 1000px; overflow: hidden; }
  body {
    position: relative;
    font-family: "Open Sans", sans-serif;
    background: var(--band-light);
  }
  .card-stage {
    position: absolute; left: 0; top: 0; width: 1200px; height: 716px;
    background: linear-gradient(180deg, var(--stage-top), var(--stage-bottom));
  }
  .card {
    position: absolute; width: 470px; height: 268px;
    background: var(--card);
    border-radius: 22px;
    box-shadow: 0 14px 30px rgba(0,0,0,.45), inset 0 0 0 1px var(--card-edge);
  }
  .card--front { left: 130px; top: 250px; }
  .card--back { left: 600px; top: 250px; }

  .wordmark {
    display: flex; flex-direction: column; align-items: center; gap: 12px;
    font-weight: 700; color: var(--ink-light);
    text-transform: uppercase; letter-spacing: .04em; line-height: 1.15; text-align: center;
  }
  .wordmark__square { background: var(--ink-light); flex: none; }

  .card--front .wordmark { position: absolute; left: 0; right: 0; top: 40px; font-size: 22px; }
  .card--front .wordmark__square { width: 72px; height: 72px; }
  .card__city { position: absolute; left: 0; right: 0; top: 196px; text-align: center; color: var(--ink-soft); font-size: 17px; }

  .card--back .wordmark { position: absolute; left: 22px; top: 50px; width: 160px; font-size: 16px; }
  .card--back .wordmark__square { width: 60px; height: 60px; }
  .contact { position: absolute; left: 200px; top: 64px; color: var(--ink-light); }
  .contact__name { font-size: 25px; font-weight: 300; }
  .contact__name strong { font-weight: 700; }
  .contact__title { font-size: 14px; color: var(--ink-soft); margin-top: 2px; }
  .contact__list { list-style: none; margin-top: 20px; }
  .contact__item { display: flex; align-items: center; gap: 10px; font-size: 13px; margin-bottom: 9px; color: var(--ink-soft); white-space: nowrap; }
  .contact__item svg { width: 15px; height: 15px; fill: var(--icon); flex: none; }

  .emblem-band {
    position: absolute; left: 0; top: 716px; width: 1200px; height: 284px;
    background: radial-gradient(ellipse at 60% 30%, var(--band-light), var(--band-dark));
  }
  .emblem {
    position: absolute; top: 34px; width: 190px; height: 220px;
    display: flex; flex-direction: column; align-items: center; justify-content: center; gap: 14px;
  }
  .emblem--flag { left: 30px; }
  .emblem--orange { right: 30px; }
  .emblem__square { width: 100px; height: 100px; }
  .emblem__name { font-weight: 700; font-size: 24px; text-align: center; text-transform: uppercase; line-height: 1.1; letter-spacing: .04em; }
  .emblem--flag .emblem__square { background: var(--emblem-red); }
  .emblem--flag .emblem__name { color: var(--emblem-red); }
  .emblem--orange .emblem__square { background: var(--emblem-orange); }
  .emblem--orange .emblem__name { color: var(--emblem-orange); }
</style>
</head>
<body>
  <section class="card-stage">
    <article class="card card--front">
      <div class="wordmark"><span class="wordmark__square"></span><span>Dorvale Haulworks LLC</span></div>
      <p class="card__city">Kent, WA</p>
    </article>

    <article class="card card--back">
      <div class="wordmark"><span class="wordmark__square"></span><span>Dorvale Haulworks LLC</span></div>
      <div class="contact">
        <h1 class="contact__name">Your <strong>Name</strong></h1>
        <p class="contact__title">Job Title</p>
        <ul class="contact__list">
          <li class="contact__item">
            <svg viewBox="0 0 16 16" aria-hidden="true"><path d="M3 2h3l1 3-2 1.5a9 9 0 0 0 4.5 4.5L11 9l3 1v3a1 1 0 0 1-1 1A12 12 0 0 1 2 3a1 1 0 0 1 1-1z"/></svg>
            <span>253-614-9026</span>
          </li>
          <li class="contact__item">
            <svg viewBox="0 0 16 16" aria-hidden="true"><path d="M1 3h14v10H1z M2 4.2v.6l6 4 6-4v-.6z" fill-rule="evenodd"/></svg>
            <span>youremail@dorvalemail.com</span>
          </li>
          <li class="contact__item">
            <svg viewBox="0 0 16 16" aria-hidden="true"><path d="M8 1a5 5 0 0 0-5 5c0 4 5 9 5 9s5-5 5-9a5 5 0 0 0-5-5zm0 7a2 2 0 1 1 0-4 2 2 0 0 1 0 4z"/></svg>
            <span>4519 N. 163rd Pl Kent, WA 98517</span>
          </li>
        </ul>
      </div>
    </article>
  </section>

  <section class="emblem-band">
    <div class="emblem emblem--flag">
      <span class="emblem__square"></span>
      <span class="emblem__name">Dorvale Haulworks LLC</span>
    </div>
    <div class="emblem emblem--orange">
      <span class="emblem__square"></span>
      <span class="emblem__name">Dorvale Haulworks LLC</span>
    </div>
  </section>
</body>
</html>
```